Branding label contest for 2 great products

I require labels for our health food treat dry packs and coffee business. The packaging at this stage consists of the follow... plastic food pouches for dry ingredients and takeaway coffee cups. The coffee cup artwork/design will be for standard small, medium and large paper takeaway coffee cups and the food pouch size 190mmW x 260mmL. the pouch design will need to be customisable to allow use across a range of products. for reference please visit www.torvimelu.com.au and instagram @torvimelu for products. I have attached our logo and business card files for your perusal.

Target Market(s)

Healthy conscious, vegan, paleo, gluten free, all round fitness fanatics and yogis

Industry/Entity Type

Business

Requirements
Must have
• Earthy tones, our logo. Rustic earthy feel. trendy artwork.
Should not have
• Bright colours

```html
<!DOCTYPE html>
<html lang="en">
<head>
<meta charset="utf-8">
<title>Torvi Melu — Product Labels</title>
<link href="https://fonts.googleapis.com/css2?family=Montserrat:wght@400;500;600&display=swap" rel="stylesheet">
<style>
  :root {
    --page: #ffffff;
    --card: #ebe6de;
    --card-speck: #e3ddd3;
    --ink: #8b5a55;
    --motif: #f6f3ee;
  }
  * { margin: 0; padding: 0; box-sizing: border-box; }
  html, body {
    width: 1200px;
    height: 1046px;
    overflow: hidden;
    background: var(--page);
    font-family: "Montserrat", sans-serif;
    color: var(--ink);
  }
  .label-sheet {
    position: relative;
    width: 1200px;
    height: 1046px;
  }
  .label {
    position: absolute;
    width: 330px;
    height: 453px;
    background:
      radial-gradient(circle at 30% 40%, var(--card-speck) 0 1px, transparent 1.5px) 0 0 / 7px 9px,
      var(--card);
    overflow: hidden;
  }
  .col-1 { left: 27px; }
  .col-2 { left: 434px; }
  .col-3 { left: 841px; }
  .row-1 { top: 30px; }
  .row-2 { top: 566px; }

  .motif {
    position: absolute;
    background: linear-gradient(200deg, var(--motif), rgba(246,243,238,0.35));
  }
  .motif--beans   { right: -10px; top: -10px; width: 130px; height: 200px; border-radius: 0 0 0 70%; }
  .motif--drizzle { right: -10px; top: -10px; width: 150px; height: 150px; border-radius: 0 0 0 100%; }
  .motif--slice   { right: -4px;  top: -4px;  width: 150px; height: 165px; clip-path: polygon(45% 0, 100% 0, 100% 100%, 0 85%); }
  .motif--cookies { right: -10px; top: 0;     width: 150px; height: 170px; border-radius: 40% 0 0 60%; }
  .motif--squares { right: -10px; top: -10px; width: 190px; height: 110px; border-radius: 0 0 0 60%; }
  .motif--loaf    { right: -4px;  top: -4px;  width: 120px; height: 140px; clip-path: polygon(35% 0, 100% 0, 100% 90%, 15% 100%, 0 40%); }

  .brand {
    position: absolute;
    left: 0;
    right: 0;
    top: 188px;
    display: flex;
    align-items: center;
    justify-content: center;
    gap: 10px;
    font-weight: 600;
    font-size: 17px;
    letter-spacing: 0.32em;
    text-transform: uppercase;
  }
  .brand-dot {
    width: 10px;
    height: 10px;
    border-radius: 50%;
    background: var(--ink);
  }
  .product {
    position: absolute;
    left: 0;
    right: 0;
    top: 355px;
    text-align: center;
  }
  .product-name {
    font-weight: 600;
    font-size: 24px;
    letter-spacing: 0.2em;
    text-transform: uppercase;
    line-height: 1;
  }
  .product-tagline {
    margin-top: 10px;
    font-weight: 500;
    font-size: 11.5px;
    letter-spacing: 0.08em;
    text-transform: uppercase;
  }
  .product-name.tight { letter-spacing: 0.1em; }
</style>
</head>
<body>
<main class="label-sheet">

  <section class="label col-1 row-1">
    <div class="motif motif--beans" role="img" aria-label="Faint coffee bean pattern"></div>
    <div class="brand"><span class="brand-dot"></span>Torvi Melu</div>
    <div class="product">
      <h2 class="product-name">Coffee</h2>
      <p class="product-tagline">Freshly ground and refreshing</p>
    </div>
  </section>

  <section class="label col-2 row-1">
    <div class="motif motif--drizzle" role="img" aria-label="Faint icing drizzle pattern"></div>
    <div class="brand"><span class="brand-dot"></span>Torvi Melu</div>
    <div class="product">
      <h2 class="product-name">Biscuits</h2>
      <p class="product-tagline">Just made and scrumptious</p>
    </div>
  </section>

  <section class="label col-3 row-1">
    <div class="motif motif--slice" role="img" aria-label="Faint cake slice with sprinkles pattern"></div>
    <div class="brand"><span class="brand-dot"></span>Torvi Melu</div>
    <div class="product">
      <h2 class="product-name">Cake</h2>
      <p class="product-tagline">Relax and enjoy :)</p>
    </div>
  </section>

  <section class="label col-1 row-2">
    <div class="motif motif--cookies" role="img" aria-label="Faint round chocolate pattern"></div>
    <div class="brand"><span class="brand-dot"></span>Torvi Melu</div>
    <div class="product">
      <h2 class="product-name">Chocs</h2>
      <p class="product-tagline">Delish and yummy</p>
    </div>
  </section>

  <section class="label col-2 row-2">
    <div class="motif motif--squares" role="img" aria-label="Faint brownie squares pattern"></div>
    <div class="brand"><span class="brand-dot"></span>Torvi Melu</div>
    <div class="product">
      <h2 class="product-name">Brownies</h2>
      <p class="product-tagline">Luscious and luxurious</p>
    </div>
  </section>

  <section class="label col-3 row-2">
    <div class="motif motif--loaf" role="img" aria-label="Faint loaf of bread pattern"></div>
    <div class="brand"><span class="brand-dot"></span>Torvi Melu</div>
    <div class="product">
      <h2 class="product-name tight">Lovely Loaves</h2>
      <p class="product-tagline">Beautifully baked</p>
    </div>
  </section>

</main>
</body>
</html>
```